Party invitation with a difference

I have recently turned 65, and I am holding a party for a number of my friends

I am looking for a stylish party invitation possibly in the guise of a rock concert admission ticket./ poster

promoting my band Blue Kettle who will be playing.at the party. We are a middle of the road covers band

I am turning 65 years so something like 65 and still Rocking ...

The party will run from 7.00pm until 11.00pm

Food platter and drink supplied.

No presents please

Date Saturday 30 June 2018
At Marlow & Pike Restaurant, 317, Fenwick Lane. Clevedon, Auckland 2671

RSVP to dennis.hartwell@plumbox.co.nz

Target Market(s)

I have a guest list

Font styles to use

Colors

Designer to choose colors to be used in the design.

Requirements
Must have
• I will want to email the invitation to my guests as well as be able to print some off .
Nice to have
• The invitation is from Dennis and Marion Hartwell
Should not have
• Not be flowery

```html
<!DOCTYPE html>
<html lang="en">
<head>
<meta charset="utf-8">
<title>Blue Kettle – 65 Years and Still Rocking</title>
<link rel="stylesheet" href="https://fonts.googleapis.com/css2?family=Poppins:wght@300;400;500;600&display=swap">
<style>
  :root {
    --backdrop: #dedede;
    --paper: #ffffff;
    --ink: #111111;
    --rock-red: #c8202c;
    --neon-cyan: #1ee3f0;
    --rule-blue: #4fb3e8;
    --night: #140a35;
    --stage-blue: #2b20b8;
    --stage-violet: #4a1a9a;
    --spot-pink: #e8206f;
  }
  * { box-sizing: border-box; margin: 0; padding: 0; }
  html, body {
    width: 1200px; height: 800px; overflow: hidden;
    background: var(--backdrop);
    font-family: "Poppins", sans-serif;
    color: var(--ink);
  }
  .ticket {
    position: absolute; left: 50px; top: 220px;
    width: 1100px; height: 360px;
    background: var(--paper);
    box-shadow: 0 6px 18px rgba(0,0,0,.25);
    display: flex;
  }
  .ticket__main {
    position: relative; width: 780px; height: 100%;
    border-right: 2px dashed var(--ink);
  }
  .concert-scene {
    position: absolute; left: 110px; top: 24px;
    width: 630px; height: 312px;
    background:
      radial-gradient(circle at 80% 12%, rgba(232,32,111,.9) 0, rgba(232,32,111,0) 32%),
      linear-gradient(35deg, var(--night) 0%, var(--stage-blue) 58%, var(--stage-violet) 100%);
  }
  .band-mark {
    position: absolute; left: 270px; top: 70px;
    display: flex; align-items: center; gap: 14px;
  }
  .band-mark__square {
    width: 26px; height: 26px;
    border: 3px solid var(--neon-cyan);
  }
  .band-mark__name {
    font-weight: 600; font-size: 46px; line-height: 1;
    color: #ffffff; letter-spacing: .5px;
  }
  .rsvp {
    position: absolute; left: 175px; top: 218px; width: 500px;
    text-align: center;
    color: var(--neon-cyan);
    font-weight: 600; font-size: 25px; line-height: 1.3;
  }
  .ticket__stub {
    flex: 1; padding: 22px 20px 0;
    text-align: center;
  }
  .headline { font-weight: 500; line-height: 1.08; }
  .headline .big { color: var(--rock-red); font-size: 36px; }
  .headline .small { font-size: 24px; }
  .rule {
    width: 170px; height: 1px; background: var(--rule-blue);
    margin: 10px auto;
  }
  .provided {
    font-weight: 500; font-size: 17px; text-transform: uppercase; letter-spacing: .3px;
  }
  .provided .initial { color: var(--rock-red); font-size: 23px; }
  .venue {
    font-weight: 300; font-size: 14px; line-height: 1.45;
  }
  .time {
    display: inline-block; margin-top: 10px;
    border: 1.5px solid var(--rock-red);
    padding: 3px 10px;
    font-weight: 500; font-size: 16px;
  }
  .date { margin-top: 10px; font-weight: 500; font-size: 17px; }
  .date .accent { color: var(--rock-red); }
  .no-presents {
    margin-top: 12px; color: var(--rock-red);
    font-weight: 500; font-size: 13px;
  }
</style>
</head>
<body>
  <article class="ticket">
    <section class="ticket__main">
      <div class="concert-scene" role="img" aria-label="Concert crowd silhouettes with raised hands under blue and pink stage lights"></div>
      <div class="band-mark">
        <span class="band-mark__square"></span>
        <span class="band-mark__name">Blue Kettle</span>
      </div>
      <p class="rsvp">RSVP to Dennis or Marion at<br>dennis.hartwell@plumbox.co.nz</p>
    </section>

    <aside class="ticket__stub">
      <h1 class="headline">
        <span class="big">65 YEARS</span> <span class="small">AND</span><br>
        <span class="small">STILL</span> <span class="big">ROCKING</span>
      </h1>
      <div class="rule"></div>
      <p class="provided"><span class="initial">D</span>rinks &amp; <span class="initial">N</span>ibbles provided</p>
      <div class="rule"></div>
      <p class="venue">At Marlow &amp; Pike Restaurant,<br>317, Fenwick Lane,<br>Clevedon, &nbsp;Auckland 2671</p>
      <p class="time">7:00PM To 11:00PM</p>
      <p class="date">Saturday <span class="accent">30 June</span> 2018</p>
      <p class="no-presents">No presents please.</p>
    </aside>
  </article>
</body>
</html>
```